Carpet cleaning company focused on high quality needs business cards

We are a growing company that just merged with another company and need to design a new business card. We do both residential as well as commercial cleaning. We do carpet, tile & grout, upholstery, hard floors, and stain & pet odor removal. We treat our customers like family and strive to achieve outstanding results with every job.

```html
<!DOCTYPE html>
<html lang="en">
<head>
<meta charset="utf-8">
<title>Hearthside Steam Cleaning – Business Cards</title>
<link rel="stylesheet" href="https://fonts.googleapis.com/css2?family=Lato:wght@400;700;900&display=swap">
<style>
  :root {
    --bg: #2b2d31;
    --card: #ffffff;
    --ink: #1b1b1b;
    --muted: #4a4a4a;
    --red: #e8403a;
    --blue: #1f7cc4;
  }
  * { margin: 0; padding: 0; box-sizing: border-box; }
  html, body {
    width: 1200px; height: 952px; overflow: hidden;
    background: var(--bg);
    font-family: "Lato", Arial, sans-serif;
  }
  .stage {
    width: 1200px; height: 952px;
    display: flex; flex-direction: column;
    align-items: center; justify-content: center; gap: 50px;
  }
  .card {
    position: relative;
    width: 700px; height: 400px;
    background: var(--card);
    border-radius: 26px;
    overflow: hidden;
  }
  /* brand lockup */
  .brand {
    position: absolute;
    display: flex; align-items: center; gap: 16px;
  }
  .brand-mark {
    width: 58px; height: 58px;
    background: var(--red);
    flex: none;
  }
  .brand-name {
    color: var(--ink);
    font-weight: 900;
    line-height: 1;
  }
  .brand-name .lead { display: block; font-size: 40px; letter-spacing: -0.5px; }
  .brand-name .sub { display: block; font-size: 19px; margin-top: 6px; letter-spacing: 0.5px; }

  .card--front .brand { left: 56px; top: 118px; }
  .card--back .brand { left: 200px; top: 150px; }

  /* stripe */
  .stripe { position: absolute; height: 4px; }
  .stripe--red { background: var(--red); }
  .stripe--blue { background: var(--blue); }
  .card--front .stripe--red { left: 0; width: 318px; top: 332px; }
  .card--front .stripe--blue { left: 318px; right: 0; top: 340px; }
  .card--back .stripe--blue { left: 0; width: 318px; top: 332px; }
  .card--back .stripe--red { left: 318px; right: 0; top: 340px; }

  /* contact block */
  .contact {
    position: absolute; left: 398px; top: 92px;
    color: var(--muted);
  }
  .contact-name {
    font-size: 25px; font-weight: 400; letter-spacing: 0.5px;
    color: var(--red); white-space: nowrap;
  }
  .contact-name strong { color: var(--blue); font-weight: 900; }
  .contact-role { font-size: 14px; margin-top: 2px; }
  .contact-rule { width: 46px; height: 2px; background: var(--blue); margin: 8px 0 14px; }
  .contact-list { list-style: none; font-size: 14px; line-height: 1.35; }
  .contact-list li { display: flex; align-items: flex-start; gap: 10px; margin-bottom: 7px; }
  .icon {
    width: 18px; height: 18px; flex: none; border-radius: 3px;
    display: flex; align-items: center; justify-content: center;
    margin-top: 1px;
  }
  .icon--blue { background: var(--blue); }
  .icon--red { background: var(--red); }
  .icon svg { width: 12px; height: 12px; fill: #fff; }
</style>
</head>
<body>
<main class="stage">

  <section class="card card--front">
    <div class="brand">
      <span class="brand-mark"></span>
      <span class="brand-name"><span class="lead">Hearthside</span><span class="sub">STEAM CLEANING</span></span>
    </div>

    <div class="contact">
      <p class="contact-name">DANIEL R. <strong>WHITFORD</strong></p>
      <p class="contact-role">Managing Director</p>
      <div class="contact-rule"></div>
      <ul class="contact-list">
        <li>
          <span class="icon icon--blue"><svg viewBox="0 0 12 12"><path d="M6 0.5a4 4 0 0 0-4 4c0 3 4 7 4 7s4-4 4-7a4 4 0 0 0-4-4zm0 5.6a1.6 1.6 0 1 1 0-3.2 1.6 1.6 0 0 1 0 3.2z"/></svg></span>
          <span>2710 Maple Ridge Avenue<br>Arlington, VA 22201</span>
        </li>
        <li>
          <span class="icon icon--red"><svg viewBox="0 0 12 12"><path d="M3 1l2 2.4-1.2 1.3a6 6 0 0 0 3.5 3.5L8.6 7 11 9l-1.3 2C5 11 1 7 1 2.3z"/></svg></span>
          <span>+00 987 654 32</span>
        </li>
        <li>
          <span class="icon icon--red"><svg viewBox="0 0 12 12"><path d="M1 2.5h10v7H1zm1 1v.3l4 2.7 4-2.7v-.3z"/></svg></span>
          <span>hello@hearthsidesteam.com</span>
        </li>
        <li>
          <span class="icon icon--red"><svg viewBox="0 0 12 12"><path d="M2 1l8 4-3.4 1 2.4 3.6-1.4 1-2.4-3.6L2.5 9.5z"/></svg></span>
          <span>www.hearthsidesteam.com</span>
        </li>
      </ul>
    </div>

    <span class="stripe stripe--red"></span>
    <span class="stripe stripe--blue"></span>
  </section>

  <section class="card card--back">
    <div class="brand">
      <span class="brand-mark"></span>
      <span class="brand-name"><span class="lead">Hearthside</span><span class="sub">STEAM CLEANING</span></span>
    </div>
    <span class="stripe stripe--blue"></span>
    <span class="stripe stripe--red"></span>
  </section>

</main>
</body>
</html>
```